Moden - Mexicali - Flower Shop

brisapetals is looking for a cool web design that has a airy, clean, mexicali feel to it.

See attached images and links for idea of what we mean with the above.

please no templates.
Updates

Target Market(s)

Local flower shop in San Diego, California

Industry/Entity Type

Shop

Requirements
Must have
• see. brisapetals.quillcart.example - I did the site and logo...I love the logo - hate the site.

Going for this feel: http://www.plumnotebook.example/tablecraft/archives/verandos.php

I also attached another site I liked- I just feel like it may be to busy.

```html
<!DOCTYPE html>
<html lang="en">
<head>
<meta charset="utf-8">
<title>brisapetals — Flower Shop</title>
<link rel="stylesheet" href="https://fonts.googleapis.com/css2?family=Arimo:wght@400;700&family=Josefin+Sans:wght@300;400&display=swap">
<style>
:root{
  --page:#ececec;
  --sheet:#ffffff;
  --ink:#222222;
  --muted:#555555;
  --teal:#2bb3c0;
  --sky:#dff3f8;
  --navy:#27304f;
  --nav-top:#f4f4f4;
  --nav-bottom:#d9d9d9;
  --line:#c9c9c9;
  --footer:#e9e9e9;
  --pink:#e0337a;
  --green:#4a9a2a;
  --blue:#1f7fc5;
}
*{box-sizing:border-box;margin:0;padding:0}
html,body{width:1200px;height:900px;overflow:hidden}
body{background:var(--page) repeating-linear-gradient(45deg,transparent 0 6px,rgba(0,0,0,.025) 6px 7px);font-family:Arimo,Arial,sans-serif;color:var(--ink);position:relative}
.sheet{position:absolute;left:60px;top:12px;width:1090px;height:863px;background:var(--sheet)}
.abs{position:absolute}
.topline{left:60px;top:12px;width:1090px;height:12px;background:var(--sky)}
.toplinks{right:58px;top:14px;font-size:9px;display:flex;gap:9px}
.search{left:898px;top:28px;width:217px;height:13px;border:1px solid var(--line);font-size:8px;padding:1px 4px;color:var(--muted)}
.search-btn{right:0;top:0;width:24px;height:11px;background:#bdbdbd}
.brand{left:130px;top:54px;display:flex;align-items:center;gap:22px;font-family:"Josefin Sans",sans-serif;font-size:24px;letter-spacing:9px;color:var(--teal)}
.brand-dot{width:34px;height:34px;border-radius:50%;background:var(--sky)}
.login{left:905px;top:44px;width:205px;height:51px;border:1px solid var(--line);padding:2px 10px;font-size:10px;color:var(--muted)}
.login input{display:block;width:186px;height:11px;border:1px solid var(--line);font-size:7px;padding:0 4px;margin-top:3px;color:#999}
.login-btn{position:absolute;right:10px;bottom:2px;width:48px;height:9px;border-radius:5px;background:#ddd;font-size:7px;text-align:center}
.nav{left:79px;top:97px;width:1053px;height:19px;background:linear-gradient(var(--nav-top),var(--nav-bottom));border:1px solid var(--line);display:flex;font-size:11px}
.nav span{padding:3px 6px 0;border-right:1px solid #aaa;white-space:nowrap}
.hero-img{left:82px;top:120px;width:340px;height:158px;background:radial-gradient(ellipse at 50% 35%,#7fd0d6,#5a63b8 55%,#fff 78%)}
.hero-title{left:443px;top:148px;font-family:"Josefin Sans",sans-serif;font-weight:300;font-size:29px;line-height:28px;color:var(--teal)}
.hero-copy{left:452px;top:204px;width:265px;font-size:8px;line-height:9px;color:var(--muted);letter-spacing:.5px}
.hero-shop{left:456px;top:229px;font-size:15px;letter-spacing:1px;display:flex;align-items:center;gap:6px}
.dots{left:660px;top:271px;display:flex;gap:3px}
.dots i{width:6px;height:6px;border-radius:50%;background:#ddd}
.dots i:first-child{background:var(--teal)}
.tile{width:199px;height:53px;border:1px solid #eee;overflow:hidden}
.tile-art{position:absolute;right:0;top:0;width:105px;height:100%}
.tile-text{position:absolute;left:8px;top:6px;font-size:14px;font-weight:700;line-height:14px;font-family:Georgia,serif}
.tile-cta{display:inline-block;margin-top:3px;font:700 7px Arimo,sans-serif;padding:1px 6px;border-radius:5px;background:#ddd;color:#333}
.side-box{border:1px solid var(--line);border-radius:4px}
.colors{left:82px;top:292px;width:258px;height:60px}
.colors h3{font-size:10px;letter-spacing:.5px;padding:4px 18px;border-bottom:1px solid var(--line)}
.colors p{font-size:8px;padding:3px 10px 0;line-height:10px;display:flex;flex-wrap:wrap;gap:0 6px}
.colors b{display:inline-block;width:8px;height:8px;border:1px solid #999;margin-right:3px;vertical-align:-1px}
.reset{left:222px;top:356px;width:113px;height:15px;border-radius:8px;background:linear-gradient(#f4f4f4,#ccc);border:1px solid #bbb;font-size:10px;text-align:center;line-height:13px}
.savings{left:80px;top:378px;width:259px;height:70px;border:1px solid #eee}
.savings-art{right:6px;top:4px;width:112px;height:62px;background:linear-gradient(#d5ecd3,#c6a36c)}
.banner{left:80px;width:260px;height:55px;border-radius:4px;color:#fff;font-weight:700}
.banner-art{left:10px;top:6px;width:90px;height:44px;border-radius:4px}
.newsletter{left:88px;top:572px;width:246px;height:40px;background:#f3f3f3;padding:2px 10px;font-size:9px}
.newsletter input{display:block;width:222px;height:12px;border:1px solid var(--line);border-radius:6px;font-size:7px;padding:0 10px;margin-top:3px}
.newsletter .go{position:absolute;right:14px;bottom:2px;width:56px;height:8px;border-radius:4px;background:#222;color:#fff;font-size:7px;text-align:center;line-height:8px}
.coupon{left:88px;top:617px;width:246px;height:41px;border:1px solid #eee}
.coupon-art{left:0;top:0;width:108px;height:40px;background:linear-gradient(90deg,#e98a2c,#7cb342)}
.card{width:232px;height:138px;background:var(--sky)}
.card h4{font-size:10px;text-align:center;height:15px;line-height:15px}
.card-art{position:absolute;left:1px;top:15px;width:230px;height:100px;background:#fff;border:1px solid #ccc}
.card-art div{position:absolute;left:80px;top:8px;width:70px;height:84px;border-radius:40% 40% 10% 10%;background:radial-gradient(#fbf7ef,#e4dac9)}
.card small{position:absolute;left:16px;top:118px;font-size:8px;font-weight:700;line-height:8px}
.price{position:absolute;right:0;bottom:0;width:76px;height:22px;background:var(--navy);color:#fff;font-size:19px;font-weight:700;text-align:center;line-height:22px}
.footer{left:60px;top:742px;width:1090px;height:96px;background:var(--footer)}
.social{left:80px;top:755px;width:165px;font-weight:700}
.fcol{top:752px;font-size:8px;line-height:8.2px;color:#444}
.fcol h5{font-size:10px;color:#222;margin-bottom:2px;letter-spacing:.3px}
</style>
</head>
<body>
<div class="sheet"></div>
<div class="abs topline"></div>
<nav class="abs toplinks"><span>Home</span><span>About Us</span><span>Contact Us</span><span>Help</span><span>PRICES EX GST</span></nav>
<div class="abs search">Search Products...<span class="abs search-btn"></span></div>

<div class="abs brand"><span>brisa</span><span class="brand-dot"></span><span>petals</span></div>

<form class="abs login">Wholesale Login<input value="Enter username or email id"><input value="Password"><span class="login-btn">Submit</span></form>

<nav class="abs nav"><span>Flowers</span><span>Greenery</span><span>Accessories</span><span>Homewares</span><span>Ribbons</span><span>Potted and Arrangements</span><span>Fillers</span><span>Fruits &amp; Berries</span><span>Glass &amp; Pots</span><span>New</span><span style="border:0">On Sale</span></nav>

<div class="abs hero-img" role="img" aria-label="Blue and teal roses in a frosted teal vase"></div>
<h1 class="abs hero-title">THE BEST<br>GIFT FLOWERS</h1>
<p class="abs hero-copy">fresh stems picked each morning and tied by hand in our studio for every gift you send</p>
<div class="abs hero-shop">shop now <svg width="14" height="14"><circle cx="7" cy="7" r="6" fill="#eee" stroke="#333"/><path d="M5 4l4 3-4 3z" fill="#333"/></svg></div>
<div class="abs dots"><i></i><i></i><i></i><i></i><i></i></div>

<div class="abs tile" style="left:733px;top:118px"><div class="tile-art" role="img" aria-label="Bouquet of mixed roses" style="background:linear-gradient(90deg,#fff,#f5c13a 40%,#e23a3a)"></div><div class="tile-text" style="color:#6fae2e">Birthday<br><span style="font-size:11px">Bouquet</span><br><span class="tile-cta" style="background:#6fae2e;color:#fff">Shop Now</span></div></div>
<div class="abs tile" style="left:936px;top:118px"><div class="tile-art" role="img" aria-label="Pink orchid arrangement" style="background:linear-gradient(90deg,#fff,#f2a9c6 50%,#d6e7b8)"></div><div class="tile-text" style="color:var(--pink)">Save More<br><span style="font-size:9px;color:#444;font-weight:400">with coupon deals</span><br><span class="tile-cta" style="background:var(--pink);color:#fff">Shop Now</span></div></div>
<div class="abs tile" style="left:733px;top:174px"><div class="tile-art" role="img" aria-label="Red flowers in a pot" style="background:radial-gradient(circle at 60% 40%,#d8343a,#7a9a3a 45%,#fff 70%)"></div><div class="tile-text" style="color:#c0262c;font-style:italic">Exclusive<br>Online Offer<br><span class="tile-cta" style="background:none;text-decoration:underline">Click here</span></div></div>
<div class="abs tile" style="left:936px;top:174px"><div class="tile-art" role="img" aria-label="Mixed floral centrepiece" style="background:radial-gradient(circle at 55% 50%,#e35a6c,#8bb24a 45%,#fff 72%)"></div><div class="tile-text" style="color:#222;font-style:italic;font-size:16px">Unique<br><span style="color:var(--pink)">Design</span><br><span class="tile-cta" style="background:none;text-decoration:underline">CLICK HERE</span></div></div>
<div class="abs tile" style="left:733px;top:229px"><div class="tile-art" role="img" aria-label="Blue daisies" style="background:radial-gradient(circle at 70% 50%,#2f8fd8,#9fd3f2 50%,#fff 75%)"></div><div class="tile-text" style="color:var(--blue);font-family:Arimo,sans-serif">New Catalog<br><span style="color:#444;font-weight:400">Offer</span><br><span class="tile-cta">Click here</span></div></div>
<div class="abs tile" style="left:936px;top:229px"><div class="tile-art" role="img" aria-label="Pink tulips" style="background:linear-gradient(90deg,#fff,#f4a3c1 45%,#8cc35a)"></div><div class="tile-text" style="color:var(--pink);font-family:Arimo,sans-serif">20% OFF<br><span style="color:#444;font-size:10px">on selected</span><br><span style="color:#222">flowers</span></div></div>

<section class="abs side-box colors"><h3>SHOP BY COLOR</h3><p><span><b></b>Red</span><span><b></b>Green</span><span><b></b>Orange</span><span><b></b>Yellow</span><span><b></b>Blue</span><span><b></b>Cyan</span><span><b></b>Black</span><span><b></b>Pink</span><span><b></b>Green</span><span><b></b>Violet</span></p></section>
<div class="abs reset">Reset Colors</div>

<div class="abs savings"><div class="abs" style="left:14px;top:6px;font:italic 12px Georgia,serif;color:#4a2d6a">Special</div><div class="abs" style="left:14px;top:18px;font-size:13px;font-weight:700;color:var(--green)">SAVINGS</div><div class="abs" style="left:14px;top:32px;font-size:7px;line-height:8px;color:#666">Fresh bunches now<br>at a lower price</div><div class="abs" style="left:14px;top:48px;font-size:9px;font-weight:700;color:var(--green)">$29.99</div><div class="abs" style="left:14px;top:59px;width:46px;height:7px;background:var(--green);color:#fff;font-size:5px;text-align:center">SHOP NOW</div><div class="abs savings-art" role="img" aria-label="White daisies in a woven basket"></div></div>

<div class="abs banner" style="top:453px;background:linear-gradient(#5ac4ef,#1578c0)"><div class="abs banner-art" role="img" aria-label="Red tulips in a vase" style="background:linear-gradient(#e8483c,#7bbf4a)"></div><div class="abs" style="left:123px;top:8px;font-size:20px;line-height:18px">FLORAL<br><span style="font-weight:400">GALLERY</span></div></div>
<div class="abs banner" style="top:512px;left:84px;width:251px;background:linear-gradient(#4f74d8,#2039a6)"><svg class="abs" style="left:14px;top:6px" width="80" height="44" viewBox="0 0 80 44"><path d="M60 12a10 10 0 1 1 14 9v5" fill="none" stroke="#f2c230" stroke-width="5"/><circle cx="74" cy="35" r="3" fill="#f2c230"/><rect x="8" y="26" width="44" height="18" rx="9" fill="#4fb0e0"/></svg><div class="abs" style="left:118px;top:10px;font-size:19px;font-weight:400">HELPFUL</div><div class="abs" style="left:118px;top:30px;font-size:11px;font-weight:400;letter-spacing:.5px">TIPS &amp; TRICKS</div></div>

<form class="abs newsletter">NEWSLETTER SIGNUP<input value="Enter your email address"><span class="go">Submit</span></form>
<div class="abs coupon"><div class="abs coupon-art" role="img" aria-label="Potted orange flowers beside a picket fence"></div><div class="abs" style="left:112px;top:3px;font-size:10px;font-weight:700;line-height:10px">SIGNUP<br>TO VERDELLA FLORAL GET<br><span style="color:#e0402a;font-size:14px">FREE $10</span><br><span style="font-size:7px">COUPON</span></div><svg class="abs" style="left:218px;top:24px" width="14" height="14"><circle cx="7" cy="7" r="6" fill="#555"/><path d="M5 4l4 3-4 3z" fill="#fff"/></svg></div>

<div class="abs card" style="left:383px;top:290px"><h4>ANTHURIUM LARGE</h4><div class="card-art" role="img" aria-label="Stem of white berries"><div></div></div><small>42539CA<br>Buy 3 more $20</small><span class="price">$50</span></div>
<div class="abs card" style="left:641px;top:290px"><h4>ANTHURIUM LARGE</h4><div class="card-art" role="img" aria-label="Stem of white berries"><div></div></div><small>42539CA<br>Buy 3 more $20</small><span class="price">$50</span></div>
<div class="abs card" style="left:899px;top:290px"><h4>ANTHURIUM LARGE</h4><div class="card-art" role="img" aria-label="Stem of white berries"><div></div></div><small>42539CA<br>Buy 3 more $20</small><span class="price">$50</span></div>
<div class="abs card" style="left:383px;top:437px"><h4>ANTHURIUM LARGE</h4><div class="card-art" role="img" aria-label="Stem of white berries"><div></div></div><small>42539CA<br>Buy 3 more $20</small><span class="price">$50</span></div>
<div class="abs card" style="left:641px;top:437px"><h4>ANTHURIUM LARGE</h4><div class="card-art" role="img" aria-label="Stem of white berries"><div></div></div><small>42539CA<br>Buy 3 more $20</small><span class="price">$50</span></div>
<div class="abs card" style="left:899px;top:437px"><h4>ANTHURIUM LARGE</h4><div class="card-art" role="img" aria-label="Stem of white berries"><div></div></div><small>42539CA<br>Buy 3 more $20</small><span class="price">$50</span></div>
<div class="abs card" style="left:383px;top:584px"><h4>ANTHURIUM LARGE</h4><div class="card-art" role="img" aria-label="Stem of white berries"><div></div></div><small>42539CA<br>Buy 3 more $20</small><span class="price">$50</span></div>
<div class="abs card" style="left:641px;top:584px"><h4>ANTHURIUM LARGE</h4><div class="card-art" role="img" aria-label="Stem of white berries"><div></div></div><small>42539CA<br>Buy 3 more $20</small><span class="price">$50</span></div>
<div class="abs card" style="left:899px;top:584px"><h4>ANTHURIUM LARGE</h4><div class="card-art" role="img" aria-label="Stem of white berries"><div></div></div><small>42539CA<br>Buy 3 more $20</small><span class="price">$50</span></div>

<footer class="abs footer"></footer>
<div class="abs social"><div style="display:flex;gap:6px;align-items:center;font-size:13px;color:var(--navy)"><span style="width:40px;height:24px;background:#dde3ee;display:inline-block;font-size:7px;font-weight:400;padding:2px">1.9k<br>Like</span>Find us on<br>Chatterly</div><div style="margin-top:14px;font-size:15px;color:#4a9ad4;padding-left:30px">Chirpnet</div></div>
<div class="abs fcol" style="left:275px"><h5>TOP CATEGORIES</h5>Candles &amp; Candle<br>Glass Vases<br>Hamper Trays &amp; Gourmet<br>Soft Plush Toys<br>Wedding &amp; Events Decorations<br>Wedding Bomboniere</div>
<div class="abs fcol" style="left:479px"><h5>COMPANY INFORMATION</h5>Candles &amp; Candle<br>Glass Vases<br>Hamper Trays &amp; Gourmet<br>Soft Plush Toys<br>Wedding &amp; Events Decorations<br>Wedding Bomboniere</div>
<div class="abs fcol" style="left:723px"><h5>HELP &amp; SUPPORT</h5>Candles &amp; Candle<br>Glass Vases<br>Hamper Trays &amp; Gourmet<br>Soft Plush Toys<br>Wedding &amp; Events Decorations<br>Wedding Bomboniere</div>
<div class="abs fcol" style="left:935px"><h5>INDUSTRY INFORMATION</h5>Candles &amp; Candle<br>Glass Vases<br>Hamper Trays &amp; Gourmet<br>Soft Plush Toys<br>Wedding &amp; Events Decorations<br>Wedding Bomboniere</div>
</body>
</html>
```